Halvering Family Dentistry
Peter K. Wadlow, DDS
Project: Halvering Family Dentistry
Halvering Family Dentistry -
Creative Brief
Professional
7182 Quillan Road, Unit C Brenwick, KY 40317
smyle7q@postvale.net

```html
<!DOCTYPE html>
<html lang="en">
<head>
<meta charset="utf-8">
<title>Halvering Family Dentistry – Business Card</title>
<link rel="stylesheet" href="https://fonts.googleapis.com/css2?family=Open+Sans:wght@400;600;700&display=swap">
<style>
  :root {
    --backdrop: #ececec;
    --card: #ffffff;
    --green: #0f8a43;
    --green-dark: #06702f;
    --green-light: #2aa55a;
    --swoosh: #e6e6e6;
    --ink: #1e1e1e;
    --ink-soft: #3a3a3a;
  }
  * { margin: 0; padding: 0; box-sizing: border-box; }
  html, body {
    width: 1200px;
    height: 811px;
    overflow: hidden;
    background: var(--backdrop);
    font-family: "Open Sans", Arial, sans-serif;
  }
  .canvas { position: relative; width: 1200px; height: 811px; }
  .card {
    position: absolute;
    left: 89px;
    top: 113px;
    width: 1029px;
    height: 587px;
    border-radius: 46px;
    background: var(--card);
    overflow: hidden;
    box-shadow: 0 2px 6px rgba(0,0,0,0.12);
  }
  .card__wave { position: absolute; inset: 0; width: 100%; height: 100%; }
  .brand {
    position: absolute;
    left: 43px;
    top: 92px;
    display: flex;
    align-items: center;
    gap: 14px;
  }
  .brand__dot {
    width: 74px;
    height: 74px;
    border-radius: 50%;
    background: var(--green);
    flex: none;
  }
  .brand__name {
    font-weight: 600;
    color: var(--ink-soft);
    font-size: 44px;
    line-height: 1.05;
    text-transform: uppercase;
    letter-spacing: 0.5px;
  }
  .brand__name span { display: block; font-size: 25px; letter-spacing: 0.6px; }
  .tagline {
    position: absolute;
    left: 43px;
    top: 191px;
    font-size: 13.5px;
    font-weight: 600;
    letter-spacing: 0.3px;
    color: var(--ink-soft);
    text-transform: uppercase;
  }
  .address {
    position: absolute;
    left: 43px;
    top: 364px;
    font-size: 26px;
    font-weight: 700;
    line-height: 37px;
    color: var(--ink);
  }
  .contact {
    position: absolute;
    left: 43px;
    top: 469px;
    font-size: 24px;
    line-height: 36px;
    color: var(--ink);
  }
  .contact__label { color: var(--green); }
  .dentist {
    position: absolute;
    right: 74px;
    top: 431px;
    text-align: right;
    font-size: 34px;
    font-weight: 600;
    line-height: 50px;
    color: var(--ink);
  }
  .dentist__title { display: block; color: var(--green); font-weight: 700; }
</style>
</head>
<body>
<main class="canvas">
  <section class="card" aria-label="Business card">
    <svg class="card__wave" viewBox="0 0 1029 587" preserveAspectRatio="none" aria-hidden="true">
      <defs>
        <linearGradient id="band" x1="0" y1="0" x2="1" y2="1">
          <stop offset="0" stop-color="#06702f"/>
          <stop offset="0.55" stop-color="#0f8a43"/>
          <stop offset="1" stop-color="#2aa55a"/>
        </linearGradient>
      </defs>
      <path d="M0,0 H1029 V345 C900,350 800,330 700,260 C590,180 520,80 380,70 C240,60 100,70 0,82 Z" fill="url(#band)"/>
      <path d="M330,360 C520,380 760,372 1029,345" fill="none" stroke="var(--swoosh)" stroke-width="5"/>
      <path d="M0,82 C100,70 240,60 380,70 C520,80 590,180 700,260 C800,330 900,350 1029,345" fill="none" stroke="var(--swoosh)" stroke-width="4"/>
    </svg>

    <div class="brand">
      <div class="brand__dot"></div>
      <div class="brand__name">Halvering <span>Family Dentistry</span></div>
    </div>
    <p class="tagline">Bright gentle care for every smile since 1991</p>

    <p class="address">7182 Quillan Road, Unit C<br>Brenwick, KY 40317</p>

    <p class="contact">
      <span class="contact__label">Phone:</span> 606-555-0186<br>
      <span class="contact__label">Email:</span> smyle7q@postvale.net
    </p>

    <p class="dentist">Peter K. Wadlow,<span class="dentist__title">DDS</span></p>
  </section>
</main>
</body>
</html>
```